Varga Lillas Physiotherapy Business Card Vienna

We need a business card design for a newly created Physiotherapy company based in Vienna Austria.
We seek a simple, modern, minimalist design without too much color variation. The font should look young/fresh, but definitely not childish or so. Since we are a starting Business, we currently haven't got a logo, if you feel like a logo would fit your design, feel free to use one, but it's not necessary.
Target Market(s)
Healthcare, young and elderly people with mobility issues
Industry/Entity Type
Health And Wellness
Contact Information for Business Card
Name: Lilla Varga
Title description: Physiotherapist
Phone num: +43 664 5290 4816
e-mail: lilla.praxis@brelomail.com
Colors
Designer to choose colors to be used in the design.
Requirements
Must have
- Final design language must be in German, basically, the Title Description needs to be "Physiotherapeutin" the other details remain as in the English Language.
Nice to have
- Simple, modern, minimalist design
Should not have
- too many colors, Obvious use of a skeleton, skull, spline

```html
<!DOCTYPE html>
<html lang="de">
<head>
<meta charset="utf-8">
<title>Lilla Varga – Physiotherapeutin</title>
<link href="https://fonts.googleapis.com/css2?family=Josefin+Sans:wght@300;400&display=swap" rel="stylesheet">
<style>
  :root {
    --backdrop: #e3e5e6;
    --card: #0b0b0b;
    --ink: #f2f2f2;
    --ink-soft: #cfcfcf;
  }
  html, body {
    margin: 0;
    width: 1200px;
    height: 778px;
    overflow: hidden;
    background: var(--backdrop);
    font-family: "Josefin Sans", sans-serif;
  }
  .canvas {
    position: relative;
    width: 1200px;
    height: 778px;
  }
  .card {
    position: absolute;
    left: 364px;
    width: 470px;
    height: 257px;
    background: var(--card);
    color: var(--ink);
  }
  .card--contact { top: 96px; }
  .card--title { top: 420px; }

  .brand-mark {
    display: block;
    fill: none;
    stroke: var(--ink);
    stroke-width: 1.6;
  }
  .brand-name {
    font-weight: 300;
    font-size: 13px;
    letter-spacing: 0.04em;
    color: var(--ink);
    white-space: nowrap;
  }

  .contact-brand {
    position: absolute;
    left: 0;
    width: 190px;
    top: 82px;
    display: flex;
    flex-direction: column;
    align-items: center;
    gap: 12px;
  }
  .divider {
    position: absolute;
    left: 190px;
    top: 65px;
    width: 1px;
    height: 130px;
    background: var(--ink-soft);
  }
  .contact-details {
    position: absolute;
    left: 212px;
    top: 82px;
  }
  .person-name {
    margin: 0 0 14px;
    font-weight: 300;
    font-size: 25px;
    letter-spacing: 0.07em;
    text-transform: uppercase;
  }
  .contact-line {
    margin: 0 0 12px;
    font-weight: 300;
    font-size: 12.5px;
    letter-spacing: 0.05em;
    color: var(--ink-soft);
  }

  .title-brand {
    position: absolute;
    left: 0;
    right: 0;
    top: 44px;
    display: flex;
    flex-direction: column;
    align-items: center;
    gap: 12px;
  }
  .job-title {
    position: absolute;
    left: 0;
    right: 0;
    top: 170px;
    margin: 0;
    text-align: center;
    font-weight: 300;
    font-size: 21px;
    letter-spacing: 0.01em;
  }
</style>
</head>
<body>
<main class="canvas">
  <section class="card card--contact" aria-label="Visitenkarte Vorderseite">
    <div class="contact-brand">
      <svg class="brand-mark" width="64" height="64" viewBox="0 0 64 64" aria-hidden="true">
        <circle cx="32" cy="32" r="30"/>
      </svg>
      <span class="brand-name">Varga Lillas</span>
    </div>
    <div class="divider"></div>
    <div class="contact-details">
      <h1 class="person-name">Lilla Varga</h1>
      <p class="contact-line">+43 664 5290 4816</p>
      <p class="contact-line">lilla.praxis@brelomail.com</p>
    </div>
  </section>

  <section class="card card--title" aria-label="Visitenkarte Rückseite">
    <div class="title-brand">
      <svg class="brand-mark" width="64" height="64" viewBox="0 0 64 64" aria-hidden="true">
        <circle cx="32" cy="32" r="30"/>
      </svg>
      <span class="brand-name">Varga Lillas</span>
    </div>
    <p class="job-title">Physiotherapeutin</p>
  </section>
</main>
</body>
</html>
```